Beer Bottles and 6 Pack Case Design

Our Brewery's name is Quarry41 Brewing. We are looking for SEVEN bottle label designs. We are making this one project because we need all seven of the bottles labels to be different, but follow the same theme (as you will see in the attachments). The same goes for the six pack case design, same theme. As an added perk for the designers, we are willing to put "design by (you or your company)" on the bottle label designs and the six pack case. This will be seen by millions!!

The following are the names of our beers:
1) Frosted Marmot
2) KiwiKazoo Jamboree
3) Pearpocket Syrup
4) Runway Fringe IPA
5) Blue Cold Godaunt
6) Androids Called Mo
7) Copper Llama Limited

Our logo is also attached, please incorporate that into the designs (OR it can go on the neck of the bottle). If you have ANY questions, do not hesitate to ask!
Updates

Budgets for 2nd and 3rd place have been increased...

Project Deadline Extended
Reason: After posting this project I got very busy with other things and have not given this the attention I should have and have not responded to questions. Therefore I am going to extend the deadline by 7 days and answer all questions the best I can..

We have increased our first place budget to $500!!! 2nd and third place still get $100 each!!

Target Market(s)

The target market will be women and men, ages 24-34 with a slight focus towards the female demographic. Our target market annual income will be classified as middle to upper-middle class ($30,000- $60,000 annually).

Industry/Entity Type

It Company

Requirements
Nice to have
• Some sort of sketch of our "Characters" incorporated into the design.
Should not have
• -Many are submitting designs for the "androids called mo" label with pictures of t-rex dinosaurs. We would like just robots, no t-rex''s. Maybe a sketch of a few robots all with a "Hi My Name Is" sticker on them (like the stickers you get when you go to a big event. I have added an example of those stickers to the project attachments).
-We like the idea of a silly sketch of a donkey (possibly with a conductor hat and a whistle, but not a must) for the Copper Llama Limited label.
-We like the idea of a silly sketch of a shaven or partially shaven chinchilla for the Frosted Marmot label.
-We like the idea of a sketch of a women''s figure from behind with apples in place of her cheeks

Please take a look at the project attachment with the Fogmill Lane beer bottle labels...we are leaning towards something along that sketch style design.

```html
<!DOCTYPE html>
<html lang="en">
<head>
<meta charset="utf-8">
<title>Quarry41 Brewing – Label Series</title>
<link rel="stylesheet" href="https://fonts.googleapis.com/css2?family=Pathway+Gothic+One&family=Oswald:wght@600&display=swap">
<style>
  :root {
    --page: #ffffff;
    --kraft: #a89a68;
    --kraft-edge: #8c7f52;
    --brand: #3b5b8c;
    --marmot: #55585c;
    --kiwi: #efe8b6;
    --pear: #c8952b;
    --runway: #7d8935;
    --godaunt: #8c2235;
    --androids: #46698c;
    --llama: #a5b2be;
  }
  * { box-sizing: border-box; margin: 0; padding: 0; }
  html, body { width: 1200px; height: 994px; overflow: hidden; background: var(--page); }
  .series { position: relative; width: 1200px; height: 994px; }

  .neck-label, .body-label {
    position: absolute;
    background: var(--kraft);
    display: flex;
    flex-direction: column;
    align-items: center;
  }
  .neck-label {
    width: 86px; height: 94px;
    justify-content: space-between;
  }
  .neck-label .stripe { width: 100%; height: 13px; background: var(--accent); }
  .body-label {
    width: 112px; height: 166px;
    border: 2px solid var(--kraft-edge);
    border-radius: 3px;
    padding-top: 38px;
  }
  .brand-mark {
    font-family: "Oswald", sans-serif;
    font-weight: 600;
    color: var(--brand);
    text-align: center;
    line-height: 1.05;
    text-transform: uppercase;
  }
  .neck-label .brand-mark { font-size: 9px; }
  .body-label .brand-mark { font-size: 13px; }
  .beer-name {
    position: absolute;
    left: 0; right: 0; top: 112px;
    height: 32px;
    background: var(--accent);
    color: var(--ink);
    font-family: "Pathway Gothic One", sans-serif;
    font-size: 13.5px;
    letter-spacing: 0.3px;
    text-transform: uppercase;
    display: flex; align-items: center; justify-content: center;
    white-space: nowrap;
  }

  .marmot   { --accent: var(--marmot);   --ink: #e2e2de; }
  .kiwi     { --accent: var(--kiwi);     --ink: #5a4f2a; }
  .pear     { --accent: var(--pear);     --ink: #4a3210; }
  .runway   { --accent: var(--runway);   --ink: #f1efdc; }
  .godaunt  { --accent: var(--godaunt);  --ink: #f6d3d8; }
  .androids { --accent: var(--androids); --ink: #eef1f5; }
  .llama    { --accent: var(--llama);    --ink: #24446c; }
</style>
</head>
<body>
<main class="series">
  <div class="neck-label marmot" style="left:128px;top:255px"><span class="stripe"></span><span class="brand-mark">Quarry41<br>Brewing</span><span class="stripe"></span></div>
  <div class="body-label marmot" style="left:109px;top:530px"><span class="brand-mark">Quarry41<br>Brewing</span><span class="beer-name">Frosted Marmot</span></div>

  <div class="neck-label kiwi" style="left:266px;top:256px"><span class="stripe"></span><span class="brand-mark">Quarry41<br>Brewing</span><span class="stripe"></span></div>
  <div class="body-label kiwi" style="left:246px;top:534px"><span class="brand-mark">Quarry41<br>Brewing</span><span class="beer-name">KiwiKazoo Jamboree</span></div>

  <div class="neck-label pear" style="left:407px;top:259px"><span class="stripe"></span><span class="brand-mark">Quarry41<br>Brewing</span><span class="stripe"></span></div>
  <div class="body-label pear" style="left:387px;top:538px"><span class="brand-mark">Quarry41<br>Brewing</span><span class="beer-name">Pearpocket Syrup</span></div>

  <div class="neck-label runway" style="left:549px;top:262px"><span class="stripe"></span><span class="brand-mark">Quarry41<br>Brewing</span><span class="stripe"></span></div>
  <div class="body-label runway" style="left:528px;top:541px"><span class="brand-mark">Quarry41<br>Brewing</span><span class="beer-name">Runway Fringe IPA</span></div>

  <div class="neck-label godaunt" style="left:692px;top:265px"><span class="stripe"></span><span class="brand-mark">Quarry41<br>Brewing</span><span class="stripe"></span></div>
  <div class="body-label godaunt" style="left:673px;top:545px"><span class="brand-mark">Quarry41<br>Brewing</span><span class="beer-name">Blue Cold Godaunt</span></div>

  <div class="neck-label androids" style="left:836px;top:269px"><span class="stripe"></span><span class="brand-mark">Quarry41<br>Brewing</span><span class="stripe"></span></div>
  <div class="body-label androids" style="left:813px;top:549px"><span class="brand-mark">Quarry41<br>Brewing</span><span class="beer-name">Androids Called Mo</span></div>

  <div class="neck-label llama" style="left:986px;top:273px"><span class="stripe"></span><span class="brand-mark">Quarry41<br>Brewing</span><span class="stripe"></span></div>
  <div class="body-label llama" style="left:966px;top:552px"><span class="brand-mark">Quarry41<br>Brewing</span><span class="beer-name">Copper Llama Limited</span></div>
</main>
</body>
</html>
```